Pell Dental Care Small Tote Bag

Pell Dental Care needs an advertisement design for a BrightMark Small Tote Bag. See website "www.pelldental.example." See uploaded files for small tote bag design template, color scheme, logos, and photo image of Dr. Pell. Designer may crop photo as necessary.

Target Market(s)

Target market is Adults ages 35 to 80.

Industry/Entity Type

Dental

Font styles to use
Sans Serif

```html
<!DOCTYPE html>
<html lang="en">
<head>
<meta charset="utf-8">
<title>Pell Dental Care – Tote Bag Print</title>
<link href="https://fonts.googleapis.com/css2?family=Lato:wght@400;700&display=swap" rel="stylesheet">
<style>
  :root {
    --canvas: #f1efe9;
    --forest: #2f5a4c;
    --sage: #6f9c8c;
    --taupe: #8a7866;
    --rule: #a9bdb5;
    --white: #ffffff;
  }
  * { margin: 0; padding: 0; box-sizing: border-box; }
  html, body {
    width: 1200px;
    height: 1000px;
    overflow: hidden;
    background: var(--canvas);
    font-family: "Lato", sans-serif;
  }
  .print-area {
    position: absolute;
    left: 190px;
    top: 110px;
    width: 820px;
    height: 780px;
  }
  .brand-name {
    text-align: center;
    color: var(--forest);
    font-weight: 700;
    line-height: 1;
  }
  .brand-name .line-main { display: block; font-size: 110px; }
  .brand-name .line-sub { display: block; font-size: 62px; margin-top: 8px; }
  .services-band {
    margin-top: 36px;
    background: var(--forest);
    color: var(--white);
    display: grid;
    grid-template-columns: 1fr 1fr;
    padding: 14px 50px;
    row-gap: 6px;
    font-size: 32px;
  }
  .services-band li { list-style: none; white-space: nowrap; }
  .services-band li::before { content: "• "; }
  .contact-row {
    display: flex;
    align-items: center;
    justify-content: center;
    gap: 18px;
    margin-top: 26px;
  }
  .tagline {
    text-align: center;
    font-size: 30px;
    line-height: 1.2;
    color: var(--taupe);
  }
  .tagline strong { color: var(--sage); font-weight: 700; display: block; }
  .phone-icon { width: 48px; height: 86px; margin-left: 16px; }
  .call-block { color: var(--forest); line-height: 1.15; }
  .call-block .call-label { font-size: 40px; }
  .call-block .call-number { font-size: 46px; font-weight: 700; }
  .divider {
    height: 2px;
    background: var(--rule);
    margin: 28px 50px 0;
  }
  .social-row {
    display: flex;
    justify-content: center;
    gap: 40px;
    margin-top: 18px;
    font-size: 38px;
    color: var(--forest);
  }
  .social-item { display: flex; align-items: center; gap: 14px; }
  .social-dot {
    width: 36px; height: 36px; border-radius: 50%;
    background: var(--sage);
  }
  .web-band {
    margin-top: 30px;
    background: var(--forest);
    color: var(--white);
    text-align: center;
    font-size: 60px;
    padding: 14px 0 18px;
  }
  .web-band b { font-weight: 700; }
</style>
</head>
<body>
  <main class="print-area">
    <h1 class="brand-name">
      <span class="line-main">Pell</span>
      <span class="line-sub">Dental Care</span>
    </h1>

    <ul class="services-band">
      <li>General Dentistry</li>
      <li>Beautiful Dentures</li>
      <li>Cosmetic Dentistry</li>
      <li>Sedation Dentistry</li>
    </ul>

    <section class="contact-row">
      <p class="tagline">Life-Changing<strong>Family Dental Care</strong>In Cedar Vale</p>
      <svg class="phone-icon" viewBox="0 0 48 86" aria-hidden="true">
        <rect x="2" y="2" width="44" height="82" rx="6" fill="var(--forest)"/>
        <rect x="8" y="10" width="32" height="34" rx="2" fill="var(--sage)"/>
        <g fill="var(--sage)">
          <rect x="8" y="50" width="8" height="6"/><rect x="20" y="50" width="8" height="6"/><rect x="32" y="50" width="8" height="6"/>
          <rect x="8" y="60" width="8" height="6"/><rect x="20" y="60" width="8" height="6"/><rect x="32" y="60" width="8" height="6"/>
          <rect x="8" y="70" width="8" height="6"/><rect x="20" y="70" width="8" height="6"/><rect x="32" y="70" width="8" height="6"/>
        </g>
      </svg>
      <div class="call-block">
        <div class="call-label">Call Us Today!</div>
        <div class="call-number">(555) 010-4827</div>
      </div>
    </section>

    <div class="divider"></div>

    <section class="social-row">
      <span class="social-item"><span class="social-dot"></span>Pell Dental Care</span>
      <span class="social-item"><span class="social-dot"></span>@PellDental</span>
    </section>

    <footer class="web-band">www.<b>pelldental</b>.example</footer>
  </main>
</body>
</html>
```